Ancient Art and Artifact information website

Hello Designers,
We are starting up a new website who talk abut and discusses an ancient arts artifacts. We would covering a wide range of countries ranging from Egypt, Greece, India, Syria, Rome, etc. My website name Brisk Loom
Designs that fits with ancient theme and some kind of uniqueness would be accepted.
Requirements:
1) A home page design
2) Sub page design
3) A suitable logo
Sections can be added are featured ancient arts/places with short description followed by a more button, latest news, and comment section.
Add contents if you found relevant for this category of website. Ability to share the information through social media is desired.
Must be a responsive design. I look forward to designs which are mind blowing.
2 page

```html
<!DOCTYPE html>
<html lang="en">
<head>
<meta charset="utf-8">
<title>Brisk Loom — Ancient Arts &amp; Artifacts</title>
<link href="https://fonts.googleapis.com/css2?family=Raleway:wght@400;500;600;700&family=Open+Sans:wght@400;600;700&display=swap" rel="stylesheet">
<style>
:root{
  --gold:#b8862e;
  --gold-light:#d4a24a;
  --header:#3a2410;
  --ink:#2a2420;
  --body-text:#3d3935;
  --white:#ffffff;
  --dark-section:#2c2215;
  --contact-bg:#141210;
  --field:#ffffff;
}
*{margin:0;padding:0;box-sizing:border-box}
html,body{width:1200px;height:3435px;overflow:hidden}
body{position:relative;background:var(--white);font-family:"Open Sans",Arial,sans-serif;color:var(--body-text)}
section,header,footer{position:absolute;left:0;width:1200px}
.abs{position:absolute}
.center{left:0;width:1200px;text-align:center}

/* header */
.site-header{top:0;height:115px;background:var(--header)}
.brand{left:240px;top:40px;width:120px;text-align:center;font-family:"Raleway",sans-serif;font-weight:600;font-size:18px;color:var(--gold-light);letter-spacing:1px}
.nav{left:424px;top:50px;display:flex;gap:30px;font-family:"Open Sans",sans-serif;font-size:11px;font-weight:600;color:var(--white);list-style:none}
.nav li:first-child{color:var(--gold-light)}

/* hero */
.hero{top:115px;height:487px;background:linear-gradient(180deg,#3b2a16 0%,#a0621a 22%,#e69a2a 42%,#f3b640 55%,#d8932c 68%,#c4801f 82%,#8a5514 100%)}
.dots{bottom:18px;display:flex;justify-content:center;gap:6px}
.dots span{width:8px;height:8px;border-radius:50%;background:rgba(255,255,255,.55)}
.dots span:first-child{background:var(--white)}

/* section titles */
.kicker{font-family:"Raleway",sans-serif;font-weight:500;letter-spacing:5px;font-size:21px;color:var(--ink)}
.kicker.light{color:var(--white)}
.title{font-family:"Raleway",sans-serif;font-weight:500;letter-spacing:9px;font-size:44px;color:var(--gold)}

/* welcome */
.welcome{top:602px;height:422px}
.welcome p{position:absolute;left:260px;width:690px;text-align:center;font-size:13px;line-height:19px;color:var(--body-text)}

/* artifacts */
.artifacts{top:1024px;height:549px;background:radial-gradient(ellipse at 50% 55%,#4a3a24 0%,#2e2417 60%,#1d170f 100%)}
.artifacts .title{font-size:34px;letter-spacing:4px}
.art-photo{border-radius:50%;border:4px solid var(--white);width:100px;height:100px}
.art-label{font-family:"Open Sans",sans-serif;color:var(--white)}
.art-label h3{font-size:15px;font-weight:700;letter-spacing:.5px}
.art-label p{font-size:11px;line-height:14px;color:#e6ddd0;width:200px;margin-top:3px}
.art-label.right{text-align:right}
.art-label.right p{margin-left:auto}
.hub{left:500px;top:280px;width:140px;height:140px;border-radius:50%;border:2px solid rgba(212,162,74,.6)}
.hub-name{left:500px;top:338px;width:140px;text-align:center;font-family:"Raleway",sans-serif;font-weight:600;font-size:18px;color:var(--gold-light)}

/* featured */
.featured{top:1573px;height:701px}
.tabs{left:0;width:1200px;top:104px;display:flex;justify-content:center;gap:18px;font-size:11px;font-weight:700;color:var(--ink);list-style:none}
.tabs li+li::before{content:"|";margin-right:18px;font-weight:400}
.grid{left:240px;top:158px;width:706px;display:grid;grid-template-columns:repeat(3,230px);grid-template-rows:231px 229px;gap:8px}

/* news */
.news{top:2274px;height:524px;background:linear-gradient(180deg,#3a2c19 0%,#5a4428 50%,#3a2c19 100%)}
.intro{left:298px;width:618px;text-align:center;font-size:12px;line-height:15px;color:#efe7da}
.news-card{top:197px;width:232px;height:269px;background:var(--white)}
.news-card .thumb{height:140px}
.news-card h3{margin:18px 12px 6px;font-size:10px;font-weight:700;color:var(--gold);letter-spacing:.5px}
.news-card p{margin:0 12px;font-size:9.5px;line-height:13px;color:var(--body-text)}

/* testimonials */
.testimonials{top:2798px;height:305px}
.portrait{left:540px;top:112px;width:110px;height:110px;border-radius:50%;border:4px solid var(--gold)}
.quote{left:290px;top:238px;width:620px;text-align:center;font-size:12px;line-height:15px;color:var(--body-text)}

/* contact */
.contact{top:3103px;height:332px;background:var(--contact-bg)}
.field{background:var(--field);font-size:8px;font-weight:700;letter-spacing:1px;color:var(--ink);padding:6px 8px}
.submit{left:261px;top:253px;width:676px;height:33px;background:var(--gold);color:var(--white);font-family:"Raleway",sans-serif;font-weight:700;font-size:11px;letter-spacing:3px;text-align:center;line-height:33px}
.copyright{left:270px;top:310px;font-size:9px;color:#cfc6b8}
</style>
</head>
<body>

<header class="site-header">
  <div class="abs brand">BRISK LOOM</div>
  <ul class="abs nav">
    <li>HOME</li><li>ABOUT US</li><li>BROWSE COUNTRY</li><li style="margin-left:10px">BLOGS</li><li>NEWS</li><li>FAQ</li><li>CONTACT US</li>
  </ul>
</header>

<section class="hero" role="img" aria-label="Desert pyramids at sunset with a camel caravan crossing the sand">
  <div class="abs dots center"><span></span><span></span><span></span><span></span></div>
</section>

<section class="welcome">
  <div class="abs center kicker" style="top:36px">WELCOME TO</div>
  <div class="abs center title" style="top:52px">BRISK LOOM</div>
  <p style="top:120px">Welcome to Brisk Loom, a place for people who love the old world. We gather stories of carved stone, painted clay and cast bronze from the great lands of the past, and we explain in plain words where each piece came from, who made it and why it still matters to us today.</p>
  <p style="top:238px">Each week our writers visit museums, digs and old city streets to bring back fresh notes and photos. Read the guides, follow the timelines and share what you find with friends who enjoy history as much as you do.</p>
  <p style="top:326px">From the tombs of the Nile to the temples of the Ganges, every region has its own voice. Browse by country, save the places you want to see and join the talk in the comments below each story.</p>
</section>

<section class="artifacts" aria-label="Ancient arts artifacts by country">
  <div class="abs center title" style="top:50px">AN ANCIENT ARTS ARTIFACTS</div>

  <div class="abs hub"></div>
  <div class="abs hub-name">BRISK LOOM</div>

  <div class="abs art-photo" style="left:458px;top:135px;background:radial-gradient(circle,#d9a45a,#8a5f2c)" role="img" aria-label="Egyptian monument"></div>
  <div class="abs art-photo" style="left:623px;top:163px;background:radial-gradient(circle,#e0b070,#9a5a2a)" role="img" aria-label="Greek temple ruins"></div>
  <div class="abs art-photo" style="left:390px;top:286px;background:radial-gradient(circle,#c9b49a,#6f6250)" role="img" aria-label="Syrian mosque"></div>
  <div class="abs art-photo" style="left:639px;top:318px;background:radial-gradient(circle,#f0ece4,#8fa8c4)" role="img" aria-label="Indian marble mausoleum"></div>
  <div class="abs art-photo" style="left:509px;top:401px;background:radial-gradient(circle,#d98a4a,#7a4020)" role="img" aria-label="Roman amphitheatre"></div>

  <div class="abs art-label right" style="right:753px;top:150px"><h3>EGYPT ANCIENT ARTS ARTIFACTS</h3><p>Carved relics and painted tombs of the Nile.</p></div>
  <div class="abs art-label" style="left:733px;top:177px"><h3>GREECE ANCIENT ARTS ARTIFACTS</h3><p>Marble statues and temples from the Aegean coast.</p></div>
  <div class="abs art-label right" style="right:820px;top:319px"><h3>SYRIA ANCIENT ARTS ARTIFACTS</h3><p>Mosaics and carved stone from the old caravan cities.</p></div>
  <div class="abs art-label" style="left:753px;top:349px"><h3>INDIA &nbsp;ANCIENT ARTS ARTIFACTS</h3><p>Temple carvings and bronze idols from many old kingdoms.</p></div>
  <div class="abs art-label right" style="right:708px;top:440px"><h3>ROME ANCIENT ARTS ARTIFACTS</h3><p>Columns, arches and frescoes of the Eternal City.</p></div>
</section>

<section class="featured">
  <div class="abs center kicker" style="top:24px;font-size:17px">ARTS PLACES</div>
  <div class="abs center title" style="top:50px">FEATURED ANCIENT</div>
  <ul class="abs tabs">
    <li>EGYPT ANCIENT PLACES</li><li>GREECE ANCIENT PLACES</li><li>INDIA ANCIENT PLACES</li><li>SYRIA ANCIENT PLACES</li><li>ROME ANCIENT PLACES</li>
  </ul>
  <div class="abs grid">
    <div role="img" aria-label="Carved marble mausoleum facade" style="background:linear-gradient(180deg,#d8d2c6,#a79c8a)"></div>
    <div role="img" aria-label="Great pyramid under blue sky" style="background:linear-gradient(180deg,#6fa6d8 0%,#b8c9d8 40%,#b88a52 55%,#8a6438 100%)"></div>
    <div role="img" aria-label="Sphinx statue against blue sky" style="background:linear-gradient(180deg,#3f7fc8 0%,#8fb6e0 45%,#b79a74 60%,#8c7258 100%)"></div>
    <div role="img" aria-label="Roman amphitheatre at sunset" style="background:linear-gradient(180deg,#e8a050 0%,#c8784a 45%,#8a5030 100%)"></div>
    <div role="img" aria-label="Baroque fountain with statues" style="background:linear-gradient(180deg,#e8d6b0 0%,#c8b088 55%,#4aa8b8 100%)"></div>
    <div role="img" aria-label="Ancient columns in front of old buildings" style="background:linear-gradient(180deg,#5a90c8 0%,#c87a4a 45%,#a8603a 100%)"></div>
  </div>
</section>

<section class="news">
  <div class="abs center kicker light" style="top:40px;font-size:21px">ARTS PLACES</div>
  <div class="abs center title" style="top:70px">LATES NEWS</div>
  <p class="abs intro" style="top:128px">Fresh reports from digs, museums and collections around the world. Find new finds, restored works and exhibitions, with short notes from our writers on what each one tells us about the people who made them.</p>

  <article class="abs news-card" style="left:224px">
    <div class="thumb" role="img" aria-label="Hillside ruins of an old city" style="background:linear-gradient(180deg,#7aa8d8,#c89460 60%,#7a6a4a)"></div>
    <h3>GREECE ANCIENT PLACES</h3>
    <p>Restorers finish work on a painted wall found under an old market. The colours are bright again and the room opens to visitors next spring.</p>
  </article>
  <article class="abs news-card" style="left:483px">
    <div class="thumb" role="img" aria-label="Roman amphitheatre in evening light" style="background:linear-gradient(180deg,#6a8fc8,#d88a4a 55%,#8a4a2a)"></div>
    <h3>ROME ANCIENT PLACES</h3>
    <p>A new survey maps the lower rooms of the great arena, showing how animals and fighters were lifted to the sand above the crowd.</p>
  </article>
  <article class="abs news-card" style="left:740px">
    <div class="thumb" role="img" aria-label="Sphinx and pyramids in the desert" style="background:linear-gradient(180deg,#8ab4dc,#d8b078 55%,#b08850)"></div>
    <h3>EGYPT ANCIENT PLACES</h3>
    <p>Teams on the plateau report a sealed shaft near the old causeway. Early scans point to tools and jars left by the ancient builders.</p>
  </article>
</section>

<section class="testimonials">
  <div class="abs center kicker" style="top:28px;font-size:25px">ARTS PLACES</div>
  <div class="abs center title" style="top:54px">TESTIMONIALS</div>
  <div class="abs portrait" role="img" aria-label="Reviewer photo placeholder showing an ancient amphitheatre" style="background:radial-gradient(circle,#d8925a,#7a4a2a)"></div>
  <p class="abs quote">Brisk Loom turned my weekend reading into a real hobby. The guides are clear, the photos are lovely and I now plan every trip around the places I first met here.</p>
</section>

<section class="contact">
  <div class="abs center kicker light" style="top:36px;font-size:24px">ARTS PLACES</div>
  <div class="abs center title" style="top:62px">CONTACT US</div>
  <div class="abs field" style="left:261px;top:125px;width:334px;height:25px">NAME *</div>
  <div class="abs field" style="left:605px;top:125px;width:332px;height:25px">EMAIL *</div>
  <div class="abs field" style="left:261px;top:157px;width:676px;height:87px">MESSAGE</div>
  <div class="abs submit">SUBMIT YOUR MESSAGE</div>
  <div class="abs copyright">Copyright 2017 Brisk Loom. All Rights Reserved.</div>
</section>

</body>
</html>
```